Business card design for immigration consulting business

We need business card design for a company called R&T Immigration Consultants Inc. This is a boutique immigration consulting and foreign recruitment agency owned and managed by two partners.
The business card will be used by partners \ owners of the business. The best way to describe the business would be committed to client, passionate about providing top-notch services, engaging, competent, professional

Target Market(s)

We work with individuals in and outside of Canada who need immigration advise as well as Canadian businesses looking to hire or sponsor foreign workers to Canada

Industry/Entity Type

Consulting

Contact Information for Business Card

The business card should have a standard size and horizontal lay-out

Font styles to use
Serif

Colors
f04a50
ec1f27
cbcbcb
dbdbdb

Requirements
Must have
• The business card mush have our logo, name of the company first and last name of the partner, position, phone, cell, fax, e-mail, skype, web-site
• Our first choice would a classic design with minimalist looks and elegant fonts and colors, but we are open minded to any creative ideas too
Nice to have
• On the other side it may have the description of the company: Immigration and Foreign Recruitment Services
• We're considering using stamping \ lettering on our business cards
• It would be nice if the business card would have white space, in case someone would like to make notes on it.
• One (back side) side of the business card can be all red with white logo
Should not have
• We do not want to have our pictures on the business card
• We do no want to have Canadian maple leaf on the business card as we already have one in our logo

```html
<!DOCTYPE html>
<html lang="en">
<head>
<meta charset="utf-8">
<title>R&amp;T Immigration – Business Cards</title>
<link rel="stylesheet" href="https://fonts.googleapis.com/css2?family=Merriweather:wght@400;700&display=swap">
<style>
  :root {
    --red: #ec1f27;
    --red-light: #f04a50;
    --grey-light: #dbdbdb;
    --grey-mid: #cbcbcb;
    --ink: #1c1c1c;
    --text: #3a3a3a;
    --icon: #5a5a5a;
    --logo-grey: #6e6e6e;
    --white: #ffffff;
    --backdrop: #2b2b2b;
  }
  * { box-sizing: border-box; margin: 0; padding: 0; }
  html, body {
    width: 1200px; height: 1087px; overflow: hidden;
    background: var(--backdrop);
    font-family: "Merriweather", Georgia, serif;
  }
  .card {
    position: absolute; left: 306px;
    width: 567px; height: 325px;
  }
  /* Front */
  .card-front { top: 203px; background: var(--white); }
  .person { position: absolute; left: 63px; top: 70px; }
  .person-name { font-size: 26px; font-weight: 700; color: var(--ink); line-height: 1.1; }
  .person-role { font-size: 16px; font-weight: 700; color: var(--ink); margin-top: 3px; }
  .accent-bar { position: absolute; left: 63px; top: 130px; width: 49px; height: 6px; background: var(--red); }
  .divider { position: absolute; left: 283px; top: 76px; width: 2px; height: 184px; background: var(--red-light); opacity: .75; }
  .front-logo {
    position: absolute; left: 326px; top: 86px;
    font-size: 24px; font-weight: 400; color: var(--logo-grey); letter-spacing: .5px;
  }
  .contact-list { position: absolute; list-style: none; top: 172px; }
  .contact-list.left { left: 63px; }
  .contact-list.right { left: 326px; }
  .contact-list li {
    display: flex; align-items: center; height: 30.5px;
    font-size: 16px; color: var(--text);
  }
  .contact-list svg { width: 17px; height: 17px; margin-right: 19px; fill: var(--icon); flex: none; }
  /* Back */
  .card-back {
    top: 573px;
    background: linear-gradient(225deg, var(--red-light) 0%, var(--red) 55%, var(--red) 100%);
    color: var(--white); text-align: center;
  }
  .back-logo {
    position: absolute; left: 0; right: 0; top: 124px;
    font-size: 44px; font-weight: 400; line-height: 1;
  }
  .tagline {
    position: absolute; left: 0; right: 0; top: 266px;
    font-size: 19px; font-weight: 400;
  }
</style>
</head>
<body>
  <section class="card card-front" aria-label="Business card front">
    <div class="person">
      <p class="person-name">Daniel Foster</p>
      <p class="person-role">President</p>
    </div>
    <span class="accent-bar"></span>
    <span class="divider"></span>

    <ul class="contact-list left">
      <li>
        <svg viewBox="0 0 24 24" aria-hidden="true"><path d="M6.6 10.8c1.4 2.8 3.8 5.1 6.6 6.6l2.2-2.2c.3-.3.7-.4 1-.2 1.1.4 2.3.6 3.6.6.6 0 1 .4 1 1V20c0 .6-.4 1-1 1C10.6 21 3 13.4 3 4c0-.6.4-1 1-1h3.5c.6 0 1 .4 1 1 0 1.3.2 2.5.6 3.6.1.3 0 .7-.2 1l-2.3 2.2z"/></svg>
        123 456 7890
      </li>
      <li>
        <svg viewBox="0 0 24 24" aria-hidden="true"><path d="M12 7C7 7 2.5 8.3 1 10.5v2.5h5v-2.5c1.9-.6 4-.9 6-.9s4.1.3 6 .9V13h5v-2.5C21.5 8.3 17 7 12 7z"/><path d="M6 14.5 4.5 19h15L18 14.5H6zm6 3.3a1.6 1.6 0 1 1 0-3.2 1.6 1.6 0 0 1 0 3.2z"/></svg>
        456 123 7890
      </li>
      <li>
        <svg viewBox="0 0 24 24" aria-hidden="true"><path d="M7 2h10v6H7z"/><path d="M3 9h18v12H3zm3 3v2h3v-2zm5 0v2h3v-2zm-5 4v2h3v-2zm5 0v2h3v-2zm5-4v6h3v-6z" fill-rule="evenodd"/></svg>
        789 456 1230
      </li>
    </ul>

    <p class="front-logo">R&amp;T Immigration</p>

    <ul class="contact-list right">
      <li>
        <svg viewBox="0 0 24 24" aria-hidden="true"><path d="M2 5h20v2l-10 6L2 7z"/><path d="M2 9l10 6 10-6v10H2z"/></svg>
        name@email.com
      </li>
      <li>
        <svg viewBox="0 0 24 24" aria-hidden="true"><circle cx="12" cy="12" r="10"/><path d="M7 8c2 0 3 1 3 2.5S8.5 13 9 15s1 4 0 5c-2-1-4-4-4-8 0-1.5.6-3 2-4zm8-3c1 1 1 2 0 3s-2 2-1 3 3 0 4 1-1 4-2 5" fill="none" stroke="#fff" stroke-width="1.4"/></svg>
        company.com
      </li>
      <li>
        <svg viewBox="0 0 24 24" aria-hidden="true"><circle cx="12" cy="12" r="10"/></svg>
        user-name
      </li>
    </ul>
  </section>

  <section class="card card-back" aria-label="Business card back">
    <p class="back-logo">R&amp;T Immigration</p>
    <p class="tagline">Immigration and Foreign Recruitment Services</p>
  </section>
</body>
</html>
```